Website Design AI Digital Marketing Tool for Small Businesses

We are a marketing saas that is selling an app that allows business owners to launch digital marketing campaigns in one click. Our value proposition is to help them grow their business in one click with pre-vetted marketers armed with AI.

We want a modern website design that looks like a professional tech startup / saas. Use the same content on plovenda.io and make it look incredible. We want it to stand out and use big bold colors and text so that it's energetic and creative but still modern.

Pages are:
Home - plovenda.io
Pricing - plovenda.io/pricing
Features - https://plovenda.io/features/
Marketing - https://plovenda.io/marketing/

EXAMPLES
https://zantrel.example-sites.io/
https://moss-venture-sample-layout.example-sites.io/home-02

We really want a professional tech company feel. It needs to look like the best company with the best team in the world created it.

Target Market(s)

We are targeting small businesses to help them with their digital marketing

Industry/Entity Type

Tech

Coding

Coded - Design and coding required

Number of Pages Required

4 page

Font styles to use
Sans Serif
Other font styles liked:
• Work Sans

Colors
0094D4
00A9DD
6FCCEA
C7EBF8
E9F6FB

Requirements
Must have
• Modern, bright colors, same / similar content as existing site
Nice to have
• Big bold text and brand colors like quillrun - but also techy and modern
Should not have
• nothing that doesnt fit the brand

```html
<!DOCTYPE html>
<html lang="en">
<head>
<meta charset="utf-8">
<title>plovenda – Automate Your Small Business Growth</title>
<link rel="stylesheet" href="https://fonts.googleapis.com/css2?family=Montserrat:wght@400;500;600;700;800&display=swap">
<style>
:root{
  --navy:#0a1838;
  --navy-deep:#071230;
  --ocean:#0b2a4e;
  --cyan:#1cd3e4;
  --cyan-2:#00a9dd;
  --blue:#0094d4;
  --sky:#6fccea;
  --ice:#e9f6fb;
  --ink:#10203a;
  --muted:#5a6478;
  --white:#ffffff;
}
*{box-sizing:border-box;margin:0;padding:0}
html,body{width:1200px;height:4511px;overflow:hidden}
body{position:relative;font-family:"Montserrat",sans-serif;color:var(--ink);background:var(--white)}
.abs{position:absolute}
a{color:inherit;text-decoration:none}

/* header & hero */
.hero{left:0;top:0;width:1200px;height:720px;background:radial-gradient(ellipse at 75% 30%,#14306a 0%,var(--navy) 55%,var(--navy-deep) 100%)}
.hero-shape{left:0;top:0}
.logo{display:flex;align-items:center;gap:10px;font-size:38px;font-weight:500;color:var(--cyan)}
.logo-mark{width:30px;height:30px;border:3px solid var(--cyan);border-radius:6px}
.site-logo{left:135px;top:20px}
.nav{left:490px;top:30px;display:flex;font-size:15px;color:#fff}
.nav a{width:112px;text-align:center;padding-bottom:6px}
.nav a.active{border-bottom:2px solid var(--cyan);width:46px;margin:0 33px}
.btn{display:inline-flex;align-items:center;gap:10px;height:36px;padding:0 20px;font-size:13px;font-weight:600;white-space:nowrap}
.btn-cyan{background:var(--cyan);color:var(--navy)}
.btn-outline{border:2px solid #fff;color:#fff}
.btn-dark{background:var(--navy);color:#fff}
.btn .dot{width:20px;height:20px;border:2px solid currentColor;border-radius:4px}
.nav-cta{left:946px;top:26px;height:34px}
.hero-title{left:128px;top:178px;font-size:40px;line-height:48px;font-weight:500;color:#fff}
.hero-title strong{font-weight:800}
.hero-title .accent{color:var(--cyan);font-weight:800}
.hero-dot{left:100px;top:214px;width:10px;height:10px;border-radius:50%;background:var(--cyan)}
.hero-sub{left:128px;top:344px;width:400px;font-size:13px;line-height:19px;color:#d8e3f5}
.hero-btns{left:128px;top:408px;display:flex;gap:12px}
.hero-art{left:560px;top:110px;width:520px;height:520px;border-radius:50% 50% 10% 10%;background:radial-gradient(circle at 50% 25%,#2fe4f0 0%,#0fa9c9 25%,#123a7a 55%,rgba(10,24,56,0) 75%)}

/* companies */
.companies-label{left:0;top:722px;width:1200px;text-align:center;font-size:17px;letter-spacing:1px;color:#7a7f92}
.companies{left:150px;top:780px;width:900px;display:flex;justify-content:space-between;align-items:center}
.brand{display:flex;align-items:center;gap:8px;font-size:22px;font-weight:600;color:#1b2340}
.brand i{width:14px;height:14px;border-radius:50%;background:var(--cyan-2);display:block}

/* features */
.features{left:0;top:880px;width:1200px;height:1000px;background:linear-gradient(180deg,#fff 0%,#eef3f9 60%,#e6edf6 100%)}
.sec-title{font-size:36px;line-height:44px;text-align:center;font-weight:500;color:var(--ink)}
.sec-title strong{font-weight:800;display:block}
.features-head{left:0;top:940px;width:1200px}
.features-sub{left:0;top:1042px;width:1200px;text-align:center;font-size:16px;color:var(--ink)}
.card{width:266px;height:180px;background:#fff;box-shadow:0 10px 30px rgba(20,40,90,.08);text-align:center;padding:68px 26px 0}
.card h3{font-size:16px;font-weight:700;margin-bottom:10px}
.card p{font-size:11px;line-height:17px;color:var(--muted)}
.card.dark{background:var(--navy);color:#fff}
.card.dark p{color:#c9d3e6}
.hex{width:100px;height:108px}
.feature-btns{left:434px;top:1652px;display:flex;gap:10px}
.wedge{left:0;top:1740px}

/* best */
.best-panel{left:0;top:1910px;width:410px;height:472px;background:linear-gradient(135deg,#2fd9ea,#13b7d3);border-radius:0 14px 14px 0}
.best-art{left:120px;top:1978px;width:432px;height:300px;border-radius:10px;background:linear-gradient(160deg,#f4f8fc,#d7e4ef)}
.best-art-inner{left:140px;top:2000px;width:392px;height:240px;border-radius:6px;background:linear-gradient(120deg,#e6f4f9,#bfe7f1 60%,#8fd6e8)}
.best-badge{left:384px;top:2218px;width:96px;height:96px;border-radius:50%;background:#fff;box-shadow:0 6px 20px rgba(0,0,0,.12);display:flex;align-items:center;justify-content:center}
.best-title{left:646px;top:1944px;font-size:36px;font-weight:500}
.best-title strong{font-weight:800}
.best-line{left:1016px;top:1974px;width:184px;height:2px;background:var(--cyan)}
.best-line::before{content:"";position:absolute;left:0;top:-4px;width:10px;height:10px;border-radius:50%;background:var(--cyan-2)}
.best-sub{left:648px;top:2004px;width:420px;font-size:16px;line-height:23px}
.promise{left:640px;top:2114px;width:458px;height:114px;border:2px solid var(--cyan);background:#fff;padding:20px 24px 0 84px}
.promise h4{font-size:16px;font-weight:600;margin-bottom:6px}
.promise p{font-size:12.5px;line-height:19px;color:var(--muted)}
.ico{width:40px;height:40px}
.best-item{left:660px;display:flex;align-items:center;gap:26px;font-size:16px;font-weight:600;width:438px;padding-bottom:16px;border-bottom:1px solid #e3e8ef}
.best-curve{left:470px;top:2380px}

/* video section */
.ai{left:0;top:2508px;width:1200px;height:636px;background:radial-gradient(ellipse at 25% 30%,#0f3c66 0%,var(--ocean) 45%,#08203e 100%)}
.ai-line{left:0;top:2636px;width:112px;height:2px;background:var(--cyan)}
.ai-line::after{content:"";position:absolute;right:-4px;top:-4px;width:10px;height:10px;border-radius:50%;background:var(--cyan)}
.ai-title{left:148px;top:2618px;font-size:36px;line-height:40px;color:#fff;font-weight:500}
.ai-title strong{font-weight:800}
.ai-sub{left:148px;top:2750px;width:340px;font-size:16px;line-height:23px;color:#e1ecf6}
.stat{color:#fff}
.stat b{display:block;font-size:36px;font-weight:500;line-height:40px}
.stat span{font-size:17px}
.ai-art{left:605px;top:2593px;width:482px;height:490px;border-radius:12px;background:linear-gradient(135deg,#1cd3e4 0%,#17a6c9 45%,#0f5f8f 100%)}
.play{left:640px;top:2908px;width:118px;height:118px;border-radius:50%;background:#ffffff;display:flex;align-items:center;justify-content:center;box-shadow:0 8px 24px rgba(0,0,0,.25)}

/* testimonials */
.t-line{left:0;top:3298px;width:108px;height:2px;background:var(--cyan)}
.t-line::after{content:"";position:absolute;right:-4px;top:-4px;width:10px;height:10px;border-radius:50%;background:var(--cyan)}
.t-title{left:130px;top:3278px;font-size:36px;line-height:44px;font-weight:500}
.t-title strong{font-weight:800;display:block}
.t-sub{left:130px;top:3382px;font-size:13.5px;line-height:21px;color:var(--muted)}
.t-arrows{left:136px;top:3456px;font-size:26px;display:flex;gap:18px;color:var(--ink)}
.t-arrows span:first-child{color:#b9c0cc}
.quote{width:308px;height:272px;background:#fff;box-shadow:0 8px 30px rgba(20,40,90,.1);border-bottom:6px solid var(--cyan);padding:26px 28px}
.quote .qm{font-size:54px;line-height:40px;font-weight:800;color:var(--cyan);height:44px}
.quote p{font-size:12px;line-height:17px;color:var(--muted);margin-top:12px}
.author{display:flex;align-items:center;gap:12px;margin-top:18px;font-size:12px}
.author i{width:34px;height:34px;border-radius:50%;background:#b8c3d3;display:block}
.author b{display:block;font-size:12px}

/* cta */
.cta{left:100px;top:3626px;width:1009px;height:518px;background:linear-gradient(135deg,#1a9fd0 0%,#19bfe0 55%,#23d8ea 100%)}
.cta-art{left:187px;top:3723px;width:438px;height:330px;border-radius:4px;background:linear-gradient(135deg,#f3ecf4,#e3dbf0 50%,#d7d0ee)}
.cta-title{left:667px;top:3752px;font-size:34px;line-height:40px;color:#fff;font-weight:500}
.cta-title strong{font-weight:800}
.cta-sub{left:669px;top:3848px;font-size:17px;line-height:24px;color:#fff}
.cta-btn{left:670px;top:3914px;height:40px}

/* footer */
.footer{left:0;top:4144px;width:1200px;height:367px;background:var(--navy)}
.f-logo{left:145px;top:4205px}
.socials{left:176px;top:4278px;display:flex;gap:12px}
.socials i{width:30px;height:30px;border-radius:50%;border:2px solid var(--cyan);display:block}
.f-col{top:4212px;padding-left:18px;border-left:2px solid var(--cyan);height:180px;color:#fff}
.f-col h5{font-size:15px;font-weight:600;margin-bottom:22px}
.f-col a{display:block;font-size:13px;margin-bottom:14px}
.f-contact{display:flex;gap:14px;font-size:12.5px;line-height:18px;margin-bottom:16px}
.f-contact i{width:26px;height:26px;border-radius:50%;background:#fff;flex:none;display:block}
.f-bottom{left:146px;top:4444px;width:925px;display:flex;justify-content:space-between;font-size:11px;color:#aeb8cc}
.f-bottom div{display:flex;gap:20px}
</style>
</head>
<body>

<!-- Hero -->
<section class="abs hero" aria-label="Hero"></section>
<svg class="abs hero-shape" width="1200" height="740" viewBox="0 0 1200 740" aria-hidden="true">
  <polygon points="0,556 360,612 0,740" fill="#1cd3e4"/>
  <polygon points="0,740 360,612 970,690 1200,708 1200,740" fill="#ffffff"/>
  <polygon points="380,612 970,688 970,696 380,620" fill="#0b1e6a"/>
</svg>
<div class="abs hero-art" role="img" aria-label="Illustration of the app emblem glowing above stacked dashboard screens with an AI chip"></div>

<header>
  <a class="abs logo site-logo" href="#"><span class="logo-mark"></span>plovenda</a>
  <nav class="abs nav">
    <a class="active" href="#">Home</a>
    <a href="#">Pricing</a>
    <a href="#">Features</a>
    <a href="#">Marketing</a>
  </nav>
  <a class="abs btn btn-cyan nav-cta" href="#">Get Started <span class="dot"></span></a>
</header>

<span class="abs hero-dot"></span>
<h1 class="abs hero-title">The App to<br>Automate Your Small<br><strong>Business</strong> <span class="accent">Growth</span></h1>
<p class="abs hero-sub">The Only Marketing Platform for Small Businesses that Handles Your Marketing in One Click.</p>
<div class="abs hero-btns">
  <a class="btn btn-cyan" href="#">Get Started <span class="dot"></span></a>
  <a class="btn btn-outline" href="#">How it works</a>
</div>

<!-- Companies -->
<p class="abs companies-label">COMPANIES WE WORK WITH</p>
<div class="abs companies">
  <span class="brand">Rankfold</span>
  <span class="brand"><i></i>Norvale Partners</span>
  <span class="brand">TradeLumen</span>
  <span class="brand">Cresthaven Academy</span>
  <span class="brand"><i></i>Peakwise</span>
</div>

<!-- Features -->
<section class="abs features" aria-label="Features"></section>
<h2 class="abs sec-title features-head">Online Marketing Will<strong>Never Be the Same</strong></h2>
<p class="abs features-sub">Get a Fortune-500 Quality Web Presence and a Personalized Action Plan</p>

<div class="abs card" style="left:158px;top:1156px"><h3>Set Your Goals</h3><p>The easiest intake form that you've ever seen. Set your goals and click submit for a custom proposal.</p></div>
<div class="abs card dark" style="left:460px;top:1156px"><h3>Get Detailed Action Plan</h3><p>Get Your Granular Action Plan / Proposal That Fits Your Parameters to Take You to the Next Level.</p></div>
<div class="abs card" style="left:762px;top:1156px"><h3>Instant Marketing</h3><p>Instantly Get Matched With One of the Top Marketing Pros in Your Industry to Help You Execute Your Campaign.</p></div>
<div class="abs card" style="left:160px;top:1428px"><h3>AI+ Web Creation</h3><p>AI Generated Marketing Campaigns &amp; Website Draft Will Be Generated to Use As a Starting Point.</p></div>
<div class="abs card" style="left:462px;top:1428px"><h3>Flexible Pricing</h3><p>No long term commitments or contracts. Subscribe month to month or only pay for what you need.</p></div>
<div class="abs card" style="left:765px;top:1428px"><h3>Launch Campaign</h3><p>Launch your marketing / business growth campaign and stay in contact to get outstanding results.</p></div>

<svg class="abs hex" style="left:241px;top:1098px" viewBox="0 0 100 108" aria-hidden="true"><polygon points="50,2 96,28 96,80 50,106 4,80 4,28" fill="#e9f6fb" stroke="#6fccea"/><polygon points="50,12 88,34 88,74 50,96 12,74 12,34" fill="#1cd3e4"/><circle cx="50" cy="54" r="16" fill="none" stroke="#fff" stroke-width="3"/><circle cx="50" cy="54" r="6" fill="#fff"/></svg>
<svg class="abs hex" style="left:543px;top:1098px" viewBox="0 0 100 108" aria-hidden="true"><polygon points="50,2 96,28 96,80 50,106 4,80 4,28" fill="#efe6fb" stroke="#b48ef0"/><polygon points="50,12 88,34 88,74 50,96 12,74 12,34" fill="#8f3ee6"/><circle cx="50" cy="54" r="16" fill="none" stroke="#fff" stroke-width="3"/><circle cx="50" cy="54" r="6" fill="#fff"/></svg>
<svg class="abs hex" style="left:845px;top:1098px" viewBox="0 0 100 108" aria-hidden="true"><polygon points="50,2 96,28 96,80 50,106 4,80 4,28" fill="#e9f6fb" stroke="#6fccea"/><polygon points="50,12 88,34 88,74 50,96 12,74 12,34" fill="#1cd3e4"/><circle cx="50" cy="54" r="16" fill="none" stroke="#fff" stroke-width="3"/><circle cx="50" cy="54" r="6" fill="#fff"/></svg>
<svg class="abs hex" style="left:243px;top:1370px" viewBox="0 0 100 108" aria-hidden="true"><polygon points="50,2 96,28 96,80 50,106 4,80 4,28" fill="#e9f6fb" stroke="#6fccea"/><polygon points="50,12 88,34 88,74 50,96 12,74 12,34" fill="#1cd3e4"/><circle cx="50" cy="54" r="16" fill="none" stroke="#fff" stroke-width="3"/><circle cx="50" cy="54" r="6" fill="#fff"/></svg>
<svg class="abs hex" style="left:545px;top:1370px" viewBox="0 0 100 108" aria-hidden="true"><polygon points="50,2 96,28 96,80 50,106 4,80 4,28" fill="#e9f6fb" stroke="#6fccea"/><polygon points="50,12 88,34 88,74 50,96 12,74 12,34" fill="#1cd3e4"/><rect x="36" y="40" width="28" height="28" rx="3" fill="none" stroke="#fff" stroke-width="3"/></svg>
<svg class="abs hex" style="left:848px;top:1370px" viewBox="0 0 100 108" aria-hidden="true"><polygon points="50,2 96,28 96,80 50,106 4,80 4,28" fill="#e9f6fb" stroke="#6fccea"/><polygon points="50,12 88,34 88,74 50,96 12,74 12,34" fill="#1cd3e4"/><path d="M50 36 L60 58 L50 54 L40 58 Z" fill="#fff"/><rect x="36" y="64" width="28" height="4" fill="#fff"/></svg>

<div class="abs feature-btns">
  <a class="btn btn-cyan" href="#">View Pricing <span class="dot"></span></a>
  <a class="btn btn-dark" href="#">Whats Include <span class="dot" style="color:#1cd3e4"></span></a>
</div>
<svg class="abs wedge" width="1200" height="170" viewBox="0 0 1200 170" aria-hidden="true">
  <polygon points="0,170 1200,0 1200,150 0,170" fill="#ffffff"/>
  <polygon points="780,108 1200,4 1200,152" fill="#0a1838"/>
</svg>

<!-- Best -->
<div class="abs best-panel"></div>
<div class="abs best-art" role="img" aria-label="Laptop showing the marketing analytics dashboard with charts and a calendar"></div>
<div class="abs best-art-inner" role="img" aria-label="Dashboard screen with line charts, progress rings and a monthly calendar"></div>
<div class="abs best-badge"><svg class="ico" viewBox="0 0 40 40" aria-hidden="true"><rect x="6" y="8" width="28" height="20" rx="2" fill="none" stroke="#0094d4" stroke-width="2.5"/><rect x="14" y="30" width="12" height="3" fill="#0094d4"/></svg></div>
<h2 class="abs best-title">Plovenda <strong>the Best</strong></h2>
<span class="abs best-line"></span>
<p class="abs best-sub">The All in One Platform to Generate Personalized Suggestions and Hire Your Dream Team to Launch Winning Campaigns.</p>
<div class="abs promise">
  <svg class="abs ico" style="left:24px;top:22px" viewBox="0 0 40 40" aria-hidden="true"><rect x="4" y="8" width="26" height="18" rx="2" fill="none" stroke="#10203a" stroke-width="2"/><circle cx="30" cy="28" r="7" fill="#1cd3e4"/><path d="M27 28 l2 2 l4-4" stroke="#fff" stroke-width="2" fill="none"/></svg>
  <h4>No More Broken Promises</h4>
  <p>We guarantee quality marketing professionals that deliver on time and communicate constantly.</p>
</div>
<div class="abs best-item" style="top:2250px"><svg class="ico" viewBox="0 0 40 40" aria-hidden="true"><circle cx="20" cy="14" r="7" fill="none" stroke="#0094d4" stroke-width="2.5"/><path d="M6 30 q14-8 28 0" stroke="#0094d4" stroke-width="2.5" fill="none"/></svg>Start at Nearly Any Budget</div>
<div class="abs best-item" style="top:2314px;border:0"><svg class="ico" viewBox="0 0 40 40" aria-hidden="true"><rect x="8" y="6" width="22" height="16" rx="2" fill="none" stroke="#0094d4" stroke-width="2.5"/><path d="M8 30 h24" stroke="#0094d4" stroke-width="2.5"/></svg>Transparency &amp; Control</div>
<svg class="abs best-curve" width="290" height="130" viewBox="0 0 290 130" aria-hidden="true"><path d="M8 0 V70 q0 20 30 22 L250 100 q30 2 30 28" fill="none" stroke="#9fdff0" stroke-width="2"/></svg>

<!-- AI website -->
<section class="abs ai" aria-label="AI website builder"></section>
<span class="abs ai-line"></span>
<h2 class="abs ai-title">Watch Plovenda AI Build<br><strong>an SEO Optimized<br>Website in Minutes</strong></h2>
<p class="abs ai-sub">Sign Up and Receive an Professional Designed Website Same Day*</p>
<div class="abs stat" style="left:148px;top:2830px"><b>4K+</b><span>Websites Built</span></div>
<div class="abs stat" style="left:374px;top:2830px"><b>2K</b><span>Consulting Hours</span></div>
<div class="abs stat" style="left:148px;top:2938px"><b>&lt;1 HR</b><span>Avg Response Time</span></div>
<div class="abs stat" style="left:374px;top:2938px"><b>99%</b><span>Satisfaction Rate</span></div>
<div class="abs ai-art" role="img" aria-label="Video preview showing a collage of AI generated small business website pages"></div>
<div class="abs play"><svg width="34" height="34" viewBox="0 0 34 34" aria-hidden="true"><polygon points="10,6 28,17 10,28" fill="#1e7de0"/></svg></div>

<!-- Testimonials -->
<span class="abs t-line"></span>
<h2 class="abs t-title">What People<strong>Are Saying</strong></h2>
<p class="abs t-sub">Just a Few Out of Thousands<br>of Happy Customers.</p>
<div class="abs t-arrows"><span>&#8249;</span><span>&#8250;</span></div>
<article class="abs quote" style="left:415px;top:3241px">
  <div class="qm">&#8220;</div>
  <p>plovenda did an excellent job recreating our website and is doing an excellent job servicing our account as well. I would highly recommend Plovenda for any business.</p>
  <div class="author"><i></i><div><b>Marcus T</b>Owner</div></div>
</article>
<article class="abs quote" style="left:757px;top:3241px">
  <div class="qm">&#8220;</div>
  <p>The migration was just as smooth as the whole experience has been working with them. I am looking forward to continuing our partnership! They'll be right there with me when I begin redesign of my website.</p>
  <div class="author"><i></i><div><b>Elena P.</b>Business Consulting</div></div>
</article>
<article class="abs quote" style="left:1104px;top:3245px">
  <div class="qm">&#8220;</div>
  <p>plovenda did an excellent job with our website and service. I would highly recommend them to any business.</p>
  <div class="author"><i></i><div><b>Daniel K</b>Owner</div></div>
</article>

<!-- CTA -->
<section class="abs cta" aria-label="Call to action"></section>
<div class="abs cta-art" role="img" aria-label="Illustrated marketing roadmap with milestone pins and a phone showing the app's file screen"></div>
<h2 class="abs cta-title">Let's Make Something<br><strong>Great Together</strong></h2>
<p class="abs cta-sub">Start With Your Free<br>Digital Marketing Roadmap.</p>
<a class="abs btn btn-dark cta-btn" href="#">Join the Revolution <span class="dot" style="color:#1cd3e4"></span></a>

<!-- Footer -->
<footer>
  <div class="abs footer"></div>
  <a class="abs logo f-logo" href="#"><span class="logo-mark"></span>plovenda</a>
  <div class="abs socials"><i aria-label="Social profile one"></i><i aria-label="Social profile two"></i><i aria-label="Social profile three"></i></div>
  <div class="abs f-col" style="left:420px"><h5>Company</h5><a href="#">Home</a><a href="#">Pricing</a><a href="#">Features</a></div>
  <div class="abs f-col" style="left:636px"><h5>Links</h5><a href="#">Marketing</a><a href="#">Web Creation</a><a href="#">Automation</a></div>
  <div class="abs f-col" style="left:844px">
    <h5>Contact Us</h5>
    <div class="f-contact"><i></i><span>Address:<br>418 Harlow Ave #12<br>Brookmere, CA 90000</span></div>
    <div class="f-contact"><i></i><span style="line-height:26px">Email: ask@plovenda.io</span></div>
  </div>
  <div class="abs f-bottom"><span>© 2023 Plovenda Labs. All Rights Reserved</span><div><a href="#">Privacy Policy</a><a href="#">Terms &amp; Conditions</a></div></div>
</footer>

</body>
</html>
```